Permanent Makeup Certificate for Lash Craft Institute Certified Artists

I need a beautifully designed certificate for my students who have successfully obtained my certification for Eyebrow Micropigmentation.

I have attached my sample certificate in InDesign format. This certificate is how I want the Certified Artist Certificate to read. My wording is extremely important for US Insurance reasons. I would like it to be in 11 x 17 inch format for USA printing.

I have also attached samples of certificates from other companies to give you an idea of how fancy I would like it to be. My company colors are pink and white, so I would like the dominant colors to be shades of pink and white. I like pink pastel combines with darker shades of pink and white. If the design calls for another color in addition to pink, that would also be great. I really like the colors in the Venmara Certificate.

I have attached a copy of my signature in .png

Target Market(s)

Beauty Industry

Industry/Entity Type

Artists

Font styles to use
Serif
Script

Colors
ffffff
f9d9e8
9bcb3c
cadf82
e667a6
e34297
eea4c8
b7a5cd

Requirements
Must have
• Wording exactly as I uploaded in InDesign file
Nice to have
• Beautiful images of female face, I am not sure if I like this idea. Just an experiement

```html
<!DOCTYPE html>
<html lang="en">
<head>
<meta charset="utf-8">
<title>Lash Craft Institute – Certificate of Excellence</title>
<link rel="stylesheet" href="https://fonts.googleapis.com/css2?family=Crimson+Text:ital,wght@0,400;0,600;1,400&family=UnifrakturMaguntia&display=swap">
<style>
  :root {
    --page-bg: #e6e7e8;
    --paper: #ffffff;
    --magenta: #a8307f;
    --pink: #d45aa3;
    --pink-soft: #e78cc0;
    --pink-pale: #efcde1;
    --ink: #1e1e1e;
    --rule: #8a8a8a;
    --photo-lip: #c24f7e;
    --photo-skin: #e3c2b3;
    --photo-eye: #b88a9a;
  }
  * { margin: 0; padding: 0; box-sizing: border-box; }
  html, body { width: 1200px; height: 881px; overflow: hidden; }
  body { background: var(--page-bg); position: relative; font-family: "Crimson Text", serif; color: var(--ink); }

  .certificate {
    position: absolute; left: 20px; top: 65px; width: 1160px; height: 750px;
    background: var(--paper); overflow: hidden;
  }
  .swoosh { position: absolute; left: 0; top: 0; width: 1160px; height: 750px; }

  .photo { position: absolute; top: 31px; height: 145px; }
  .photo--lips-a { left: 292px; width: 168px; background: linear-gradient(160deg, var(--photo-skin), var(--photo-lip) 55%, #f2dde2); }
  .photo--eye { left: 469px; width: 133px; background: linear-gradient(170deg, var(--photo-skin), var(--photo-eye) 60%, #f1e2dc); }
  .photo--portrait { left: 611px; width: 161px; background: linear-gradient(180deg, #d7b3a4, var(--photo-skin) 55%, #c9898f); }
  .photo--lips-b { left: 781px; width: 167px; background: linear-gradient(165deg, var(--photo-skin), var(--photo-lip) 50%, #f4e6e6); }
  .photo--model { left: 953px; top: 0; width: 207px; height: 270px; background: radial-gradient(ellipse at 55% 45%, #ead0c4, #dfb7a5 55%, rgba(255,255,255,0) 80%); }

  .brand-name {
    position: absolute; left: 97px; top: 330px; width: 320px; text-align: center;
    font-family: "Crimson Text", serif; font-weight: 400; font-size: 40px; line-height: 1; color: var(--magenta);
  }

  .divider { position: absolute; left: 493px; top: 307px; width: 1px; height: 387px; background: var(--rule); }

  .signature-block { position: absolute; left: 153px; top: 478px; width: 203px; text-align: center; }
  .signature-mark { height: 36px; margin: 0 20px 10px; background: linear-gradient(90deg, rgba(40,40,40,0), rgba(40,40,40,.18), rgba(40,40,40,0)); }
  .signature-rule { height: 1px; background: var(--ink); }
  .signer { font-size: 15px; line-height: 16.5px; padding-top: 4px; }
  .signer__name { font-style: italic; }

  .date-block { position: absolute; left: 180px; top: 672px; width: 151px; text-align: center; }
  .date-block .signature-rule { margin-bottom: 4px; }
  .date-label { font-size: 15px; }

  .title {
    position: absolute; left: 541px; top: 348px; width: 540px;
    font-family: "UnifrakturMaguntia", serif; font-size: 47px; line-height: 1; color: var(--magenta); white-space: nowrap;
  }
  .title-rule { position: absolute; left: 683px; top: 409px; width: 252px; height: 2px; background: var(--pink); }
  .title-flourish { position: absolute; left: 786px; top: 401px; width: 46px; height: 18px; background: var(--paper); }
  .title-flourish::after { content: ""; position: absolute; inset: 3px 2px; background: var(--pink-soft); border-radius: 50%; opacity: .8; }

  .award { position: absolute; left: 598px; top: 482px; width: 560px; }
  .award__lead { font-size: 16px; letter-spacing: .06em; text-transform: uppercase; }
  .award__name { font-size: 31px; letter-spacing: .04em; text-transform: uppercase; margin-top: 28px; line-height: 1; }
  .award__text { font-size: 17px; line-height: 25.5px; margin-top: 20px; }
  .award { left: 598px; }
</style>
</head>
<body>
<main class="certificate">
  <svg class="swoosh" viewBox="0 0 1001 647" preserveAspectRatio="none" aria-hidden="true">
    <defs>
      <linearGradient id="bandGradient" x1="0" y1="0" x2="1" y2="0">
        <stop offset="0" stop-color="#c9579e"/>
        <stop offset="1" stop-color="#9c2f7f"/>
      </linearGradient>
    </defs>
    <path d="M0 4 C120 0 220 10 300 60 L300 72 C220 35 120 30 0 40 Z" fill="#c8559c"/>
    <path d="M0 46 C160 38 330 70 470 150 L470 158 C330 90 160 70 0 78 Z" fill="#efcde1"/>
    <path d="M0 84 C200 70 380 120 560 205 C640 240 700 240 760 232 L760 242 C680 258 610 250 520 222 C380 165 230 125 120 150 C60 165 20 210 0 280 Z" fill="url(#bandGradient)"/>
    <path d="M640 236 C780 230 900 205 1001 162 L1001 182 C900 222 780 244 640 242 Z" fill="#a8307f"/>
  </svg>

  <div class="photo photo--lips-a" role="img" aria-label="Close-up photograph of glossy pink lips"></div>
  <div class="photo photo--eye" role="img" aria-label="Close-up photograph of an eye with pink eyeshadow and lashes"></div>
  <div class="photo photo--portrait" role="img" aria-label="Photograph of a woman with closed eyes and pink makeup"></div>
  <div class="photo photo--lips-b" role="img" aria-label="Close-up photograph of a smile with pink lipstick"></div>
  <div class="photo photo--model" role="img" aria-label="Photograph of a woman model resting on her arm"></div>

  <div class="brand-name">Lash Craft Institute</div>

  <div class="signature-block">
    <div class="signature-mark" role="img" aria-label="Handwritten signature of Clara Rose Devlin"></div>
    <div class="signature-rule"></div>
    <p class="signer">
      <span class="signer__name">Clara Rose Devlin</span><br>
      Master Instructor<br>
      Lash Craft International<sup>®</sup>
    </p>
  </div>

  <div class="date-block">
    <div class="signature-rule"></div>
    <p class="date-label">Date</p>
  </div>

  <div class="divider"></div>

  <h1 class="title">Certificate of Excellence</h1>
  <div class="title-rule"></div>
  <div class="title-flourish" role="img" aria-label="Small decorative flourish"></div>

  <section class="award">
    <p class="award__lead">This is to certify that</p>
    <p class="award__name">Amelia Hart</p>
    <p class="award__text">
      Has successfully proven to be an<br>
      Artist of the Highest Standard in Eyebrow Micropigmentation<br>
      using the LASH CRAFT INTERNATIONAL<sup>®</sup><br>
      Microblading Method
    </p>
  </section>
</main>
</body>
</html>
```